Tallowmere Office Partners needs a new interactive and interesting website

We need an interesting, professional, modern and functional company website for Tallowmere Office Partners - a young IT Services company based out of Chennai, India.

Tallowmere Office Partners is a fully owned subsidiary of Hollin Cellarworks, one of the world's leading direct to consumer wine merchant.

We already have a registered company logo which must feature in the website.

We conceive, design, develop, test, implement and support IT solutions across the entire Hollin Cellarworks IT landscape. For ex : We currently run about 25 e-commerce websites for Hollin Cellarworks on KVM and Dot Net.

We would like to see our corporate colors used in the website. (Burgundy wine and wine green - source: www.tallowmereop.example)

We are looking at this website to communicate a fun, friendly and professionally managed company - reaching out to career seekers, prospective customers and general public.

For reference - The company name 'Tallowmere' is an inspiration from the Hollin Cellarworks lineage.

The second image with the world map is stickered on our main entrance to the office, I am not sure where this can be used -just putting it out there..
Updates

Please note that there are only a few more days to submit designs for this contest  !

I would appreciate if you can help posting your designs in time for our review and consideration.

Thanks.

Reason: Thanks for your inputs. We have a number of designers and a lot to digest and work with in the past few days. There has been a rush of new designs in the last few days Hence we will require more time to process these and make our decision. Hence i am requesting the contest to be open for more days. Regards, Suresh

Target Market(s)

Prospective job seekers who want to know more about the company and also wish to apply for a job vacancy
People wanting to know more about the company in general and our progress
People who want to see what we offer and how we can help them too - prospective customers
Companies that are interested in our IT Captive journey and are looking for a business opportunity

Industry/Entity Type

E-Commerce

Requirements
Must have
• Log In/ Register facility acting as a Single Sign on for Intranet (Employees)

Facility to post job vacancies (with an expiry date) and enable people to apply for a role and upload their CV/Resume.

Facility to Review Job applications

Facility for website visitors to contact Tallowmere Office Partners via an online 'Contact Us' form with a split of job seekers and business opportunities

Gallery facility to upload pictures regarding company events
Nice to have
• Less Cluttered and contemporary design
Some Wine/Vineyard inspirations will be good but not too much, the company is an IT services company

```html
<!DOCTYPE html>
<html lang="en">
<head>
<meta charset="utf-8">
<title>Tallowmere Office Partners</title>
<link href="https://fonts.googleapis.com/css2?family=Arimo:wght@400;700&family=Montserrat:wght@400;600&display=swap" rel="stylesheet">
<style>
  :root{
    --burgundy:#9b005e;
    --olive:#9c9f4a;
    --olive-dark:#8f9240;
    --title-box:#8f8c69;
    --panel:#f7f7f7;
    --panel-border:#dedede;
    --band:#f1f1f1;
    --ink:#1c1c1c;
    --muted:#8a8a8a;
    --icon:#333;
    --photo:#8c8c8c;
  }
  *{box-sizing:border-box;margin:0;padding:0}
  html,body{width:1200px;height:1000px;overflow:hidden;background:#fff}
  body{position:relative;font-family:"Arimo",Arial,sans-serif;color:var(--ink)}
  .abs{position:absolute}

  .topbar{left:0;top:0;width:1200px;height:47px;background:var(--burgundy)}
  .brand{left:190px;top:9px;color:#fff;line-height:1}
  .brand-mark{display:inline-block;width:14px;height:14px;border-radius:50%;background:#fff;vertical-align:top;margin:4px 5px 0 0}
  .brand-name{display:inline-block;font-size:19px;font-weight:700;vertical-align:top}
  .brand-sub{display:block;font-size:11px;margin:3px 0 0 19px}
  .nav{left:331px;top:0;height:47px;display:flex}
  .nav a{display:block;height:47px;line-height:47px;padding:0 14px;color:#fff;font-size:11px;text-decoration:none}
  .nav a.active{background:var(--olive)}
  .search{left:793px;top:13px;width:158px;height:21px;background:#fff;border-radius:3px;font-size:11px;color:#aaa;padding:4px 12px}
  .submit{left:956px;top:13px;width:61px;height:21px;background:var(--olive);border-radius:3px;color:#fff;font-size:11px;text-align:center;line-height:21px}

  .hero{left:0;top:47px;width:1200px;height:213px;background:var(--olive)}
  .hero-title{left:310px;top:97px;width:588px;height:38px;background:var(--title-box);color:var(--burgundy);font-size:37px;font-weight:700;text-align:center;line-height:38px}
  .hero-lead{left:243px;top:142px;width:720px;height:40px;background:var(--title-box);color:var(--burgundy);font-size:11.5px;font-weight:700;text-align:center;line-height:40px}
  .hero-cta{left:542px;top:195px;width:123px;height:29px;background:var(--burgundy);border:2px solid #e7b9d6;border-radius:3px;color:#fff;font-size:13px;text-align:center;line-height:25px}

  .feature{top:285px;width:258px;height:159px;background:var(--panel);border:1px solid var(--panel-border);text-align:center}
  .feature svg{position:absolute;left:50%;top:-16px;transform:translateX(-50%)}
  .feature h3{margin-top:55px;font-family:"Montserrat",Arial,sans-serif;font-weight:600;font-size:17px}
  .feature p{margin:7px auto 0;width:215px;font-size:11px;line-height:12px;color:var(--muted)}

  .section-title{font-family:"Montserrat",Arial,sans-serif;font-size:13px;color:var(--ink);display:flex;align-items:center;gap:7px}
  .grid-icon{width:13px;height:13px;display:grid;grid-template-columns:6px 6px;gap:1px}
  .grid-icon i{background:var(--ink)}
  .team-rule{left:190px;top:517px;width:826px;height:1px;background:#e2e2e2}
  .member{top:530px;width:190px;text-align:center;font-size:11px;line-height:12px}
  .portrait{width:186px;height:112px;margin:0 auto;border-radius:93px 93px 0 0;background:#ececec;padding:7px 7px 0;overflow:hidden}
  .portrait div{width:172px;height:172px;border-radius:50%;background:radial-gradient(circle at 50% 40%,#b5b5b5,var(--photo) 60%,#5b5b5b)}
  .member b{display:block;margin-top:3px}

  .clients{left:0;top:700px;width:1200px;height:258px;background:var(--band)}
  .pager{left:946px;top:724px;width:71px;height:21px;border:1px solid #333;border-radius:3px;background:#fff;display:flex}
  .pager span{flex:1;display:flex;align-items:center;justify-content:center}
  .pager span+span{border-left:1px solid #333}
  .client{width:193px;height:85px;background:#fff;border:1px solid #dcdcdc;display:flex;align-items:center;justify-content:center;font-size:15px;font-weight:700;color:#7d1a2e;text-align:center}

  .footer{left:0;top:958px;width:1200px;height:42px;background:#fff;font-size:11px}
  .footer .copy{position:absolute;left:190px;top:14px;color:#333}
  .footer .links{position:absolute;right:184px;top:14px;color:var(--burgundy)}
</style>
</head>
<body>
  <header class="abs topbar">
    <div class="abs brand"><span class="brand-mark"></span><span class="brand-name">tallowmere</span><span class="brand-sub">Office Partners</span></div>
    <nav class="abs nav">
      <a class="active" href="#">Home</a><a href="#">About Us</a><a href="#">Services</a><a href="#">Careers</a><a href="#">Contact Us</a>
    </nav>
    <div class="abs search">Search</div>
    <div class="abs submit">Submit</div>
  </header>

  <section class="abs hero"></section>
  <h1 class="abs hero-title">Delivering IT Excellence</h1>
  <p class="abs hero-lead">Welcome to Tallowmere Office Partners, an emerging provider of global IT consulting and software services.</p>
  <div class="abs hero-cta">Learn More !</div>

  <article class="abs feature" style="left:190px">
    <svg width="82" height="60" viewBox="0 0 82 60"><path d="M4 58 C20 40 34 28 50 20 C36 30 26 40 14 54 C34 58 62 46 80 2 C48 6 24 14 18 44 Z" fill="var(--icon)"/></svg>
    <h3>Responsive Layouts</h3>
    <p>Lorem ipsum dolor sit amet, consectetur adipisicing elit, sed do eiusmod tempor incididunt ut labore et dolore magna aliqua. Ut enim ad minim veniam.</p>
  </article>
  <article class="abs feature" style="left:474px">
    <svg width="70" height="60" viewBox="0 0 70 60"><path d="M34 2 C44 14 58 22 58 40 C58 52 48 58 36 58 C22 58 12 50 12 38 C12 28 18 22 24 18 C24 26 26 30 30 32 C28 22 30 10 34 2 Z M36 54 C44 54 48 48 46 40 C44 34 40 32 38 28 C38 36 32 38 30 44 C30 50 32 54 36 54 Z" fill="var(--icon)" fill-rule="evenodd"/></svg>
    <h3>Exquisite Design</h3>
    <p>Lorem ipsum dolor sit amet, consectetur adipisicing elit, sed do eiusmod tempor incididunt ut labore et dolore magna aliqua. Ut enim ad minim veniam.</p>
  </article>
  <article class="abs feature" style="left:759px">
    <svg width="82" height="60" viewBox="0 0 82 60"><path d="M78 4 L4 34 L26 38 L30 58 L40 44 L52 56 Z M30 38 L70 10 L34 44 L32 52 Z" fill="var(--icon)" fill-rule="evenodd"/></svg>
    <h3>Clean Code</h3>
    <p>Lorem ipsum dolor sit amet, consectetur adipisicing elit, sed do eiusmod tempor incididunt ut labore et dolore magna aliqua. Ut enim ad minim veniam.</p>
  </article>

  <h2 class="abs section-title" style="left:557px;top:491px"><span class="grid-icon"><i></i><i></i><i></i><i></i></span>Our Team</h2>
  <div class="abs team-rule"></div>

  <div class="abs member" style="left:187px"><div class="portrait"><div role="img" aria-label="Portrait photo of Suresh Raghavan"></div></div><b>Suresh Raghavan</b>Head of Delivery Centre<br><strong>Tallowmere</strong> Office Partners</div>
  <div class="abs member" style="left:401px"><div class="portrait"><div role="img" aria-label="Portrait photo of Colin Ashworth"></div></div><b>Colin Ashworth</b>VP - HR &amp; Communications<br><strong>Tallowmere</strong> Office Partners</div>
  <div class="abs member" style="left:615px"><div class="portrait"><div role="img" aria-label="Portrait photo of Peter Ormsby"></div></div><b>Peter Ormsby</b>Chief Information Officer</div>
  <div class="abs member" style="left:828px"><div class="portrait"><div role="img" aria-label="Portrait photo of Neil Harcourt"></div></div><b>Neil Harcourt</b>Head of IT Services</div>

  <section class="abs clients"></section>
  <h2 class="abs section-title" style="left:190px;top:723px"><span class="grid-icon"><i></i><i></i><i></i><i></i></span>Our Client</h2>
  <div class="abs pager">
    <span><svg width="8" height="10" viewBox="0 0 8 10"><path d="M7 0 L1 5 L7 10 Z" fill="#111"/></svg></span>
    <span><svg width="8" height="10" viewBox="0 0 8 10"><path d="M1 0 L7 5 L1 10 Z" fill="#111"/></svg></span>
  </div>

  <div class="abs client" style="left:177px;top:761px">Brackenford Wine</div>
  <div class="abs client" style="left:397px;top:761px">Saltmarsh Wines</div>
  <div class="abs client" style="left:617px;top:761px">Ledgerline Wine</div>
  <div class="abs client" style="left:837px;top:761px">Calloway</div>
  <div class="abs client" style="left:177px;top:858px">Weekend Post<br>Wine Club</div>
  <div class="abs client" style="left:397px;top:858px">Hollin<br>Cellarworks</div>
  <div class="abs client" style="left:617px;top:858px">Maison Orvel</div>
  <div class="abs client" style="left:837px;top:858px">Verdin Wine</div>

  <footer class="abs footer">
    <span class="copy">Copyright © 2013 Tallowmere Office Partners Private Limited.</span>
    <span class="links">Home - About Us - Clients - Services - Careers - Contact Us</span>
  </footer>
</body>
</html>
```